Dalton Perriwether breaking. Or D. Perriwether breaking

I break in and train horses, any age any bread of horse, for any disaplin. I need a business card that is simple but effective, in the way of looking professional. I would like a horse on my card, preferably a horse without a rider. I also pre train horse, younge horses that need a bit of riding before they go into serious work, and prepare yearlings for sale.

Reason: This is for my boyfriend, and I really want it to be perfect and impressive!

Target Market(s)

Thoroughbred race horse trainers, horse industrie people.

Industry/Entity Type

Business

Contact Information for Business Card

Dalton Perriwether horse breaking, "WOLLOMBEE" Kelvale, give your horse the right start to any career. dperri@mailzone.com.au, 0481392067. Horse breaking~pre-training~sale preparation

```html
<!DOCTYPE html>
<html lang="en">
<head>
<meta charset="utf-8">
<title>D. Perriwether Breaking – Business Card</title>
<link rel="stylesheet" href="https://fonts.googleapis.com/css2?family=Exo+2:wght@400;500&family=Caveat:wght@500;700&display=swap">
<style>
  :root {
    --bg: #e4e5e7;
    --card-top: #141312;
    --card-bottom: #0c0b0a;
    --band: #1b1a18;
    --gold: #d4aa3c;
    --gold-soft: #c9a43f;
    --white: #f4f4f2;
    --grey: #c9c9c9;
  }
  * { margin: 0; padding: 0; box-sizing: border-box; }
  html, body { width: 1200px; height: 861px; overflow: hidden; }
  body {
    background: var(--bg);
    display: flex;
    align-items: center;
    justify-content: center;
  }
  .business-card {
    position: relative;
    width: 900px;
    height: 500px;
    background: linear-gradient(180deg, var(--card-top) 0%, var(--card-bottom) 100%);
    box-shadow: 0 18px 40px rgba(0,0,0,.35);
    overflow: hidden;
    color: var(--white);
  }
  .lower-band {
    position: absolute;
    left: 0; right: 0; top: 232px; bottom: 0;
    background: linear-gradient(180deg, var(--band) 0%, var(--card-bottom) 100%);
  }
  .brand {
    position: absolute;
    top: 58px;
    left: 0; right: 0;
    display: flex;
    justify-content: center;
    align-items: center;
    gap: 22px;
  }
  .brand-mark {
    width: 100px; height: 100px;
    border-radius: 50%;
    background: var(--gold);
  }
  .brand-name {
    font-family: "Exo 2", sans-serif;
    font-weight: 500;
    font-size: 40px;
    line-height: 1;
    color: var(--gold);
  }
  .services {
    position: absolute;
    top: 196px; left: 0; right: 0;
    text-align: center;
    font-family: "Exo 2", sans-serif;
    font-size: 17px;
    color: var(--grey);
    letter-spacing: .3px;
  }
  .services .dot { color: var(--white); margin: 0 4px; }
  .owner {
    position: absolute;
    top: 250px; left: 0; right: 0;
    text-align: center;
  }
  .owner-name {
    font-family: "Caveat", cursive;
    font-weight: 700;
    font-size: 60px;
    line-height: 1;
  }
  .owner-role {
    font-family: "Exo 2", sans-serif;
    font-weight: 500;
    font-size: 24px;
    margin-top: 4px;
  }
  .contact-row {
    position: absolute;
    top: 380px; left: 0; right: 0;
    display: flex;
    justify-content: center;
    gap: 26px;
    list-style: none;
    font-family: "Exo 2", sans-serif;
    font-size: 24px;
  }
  .contact-item { display: flex; align-items: center; gap: 6px; }
  .contact-icon { width: 28px; height: 28px; }
  .tagline {
    position: absolute;
    top: 430px; left: 0; right: 0;
    text-align: center;
    font-family: "Caveat", cursive;
    font-weight: 500;
    font-size: 34px;
    color: var(--gold-soft);
  }
</style>
</head>
<body>
  <article class="business-card">
    <div class="lower-band"></div>

    <header class="brand">
      <span class="brand-mark"></span>
      <h1 class="brand-name">D. Perriwether Breaking</h1>
    </header>

    <p class="services">HORSE BREAKING <span class="dot">•</span> PRE-TRAINING <span class="dot">•</span> SALE PREPARATION</p>

    <section class="owner">
      <h2 class="owner-name">Dalton Perriwether</h2>
      <p class="owner-role">Horse Breaker</p>
    </section>

    <ul class="contact-row">
      <li class="contact-item">
        <svg class="contact-icon" viewBox="0 0 28 28" aria-hidden="true">
          <circle cx="14" cy="14" r="12.5" fill="none" stroke="#f4f4f2" stroke-width="2"/>
          <path d="M7 14 L14 7.5 L21 14 M9.5 12.5 V20 H18.5 V12.5" fill="none" stroke="#f4f4f2" stroke-width="2" stroke-linejoin="round"/>
        </svg>
        <span>Wollombee, Kelvale</span>
      </li>
      <li class="contact-item">
        <svg class="contact-icon" viewBox="0 0 28 28" aria-hidden="true">
          <circle cx="14" cy="14" r="12.5" fill="none" stroke="#f4f4f2" stroke-width="2"/>
          <path d="M10 8 L12.5 11 L11 13 Q13 16.5 15.5 17 L17 15.5 L20 18 L18 20.5 Q11 20 7.5 10.5 Z" fill="#f4f4f2"/>
        </svg>
        <span>0481392067</span>
      </li>
      <li class="contact-item">
        <svg class="contact-icon" viewBox="0 0 28 28" aria-hidden="true">
          <circle cx="14" cy="14" r="12.5" fill="none" stroke="#f4f4f2" stroke-width="2"/>
          <rect x="7.5" y="9.5" width="13" height="9" fill="none" stroke="#f4f4f2" stroke-width="1.8"/>
          <path d="M7.5 9.5 L14 15 L20.5 9.5" fill="none" stroke="#f4f4f2" stroke-width="1.8"/>
        </svg>
        <span>dperri@mailzone.com.au</span>
      </li>
    </ul>

    <p class="tagline">Give your horse the right start to any career.</p>
  </article>
</body>
</html>
```